Half page (a5) ad for a company

I need a design for an ad for a company to be published in a conference catalogue. Please find enclosed the logo for a company. The company is providing health screening services. Ad should be subtle and minimalistic, i.e. logo in the centre and a phrase saying: "Be in charge of your own health" and the website vantolix.co.uk. Also please find enclosed guidlines for colours and fonts to be used.

```html
<!DOCTYPE html>
<html lang="en">
<head>
<meta charset="utf-8">
<title>Vantolix – Health Screening Ad</title>
<link rel="stylesheet" href="https://fonts.googleapis.com/css2?family=Montserrat:ital,wght@0,300;0,400;0,600;1,300&display=swap">
<style>
  :root {
    --ink: #050507;
    --brand-red: #e3161f;
    --photo-red: #9a1014;
    --paper-white: #ffffff;
    --muted-white: #e8e8e8;
  }
  html, body {
    margin: 0;
    padding: 0;
    overflow: hidden;
    background: var(--ink);
  }
  .ad {
    position: relative;
    width: 846px;
    height: 1200px;
    background: var(--ink);
    overflow: hidden;
    font-family: "Montserrat", sans-serif;
  }
  .hero-photo {
    position: absolute;
    left: 150px;
    top: 290px;
    width: 546px;
    height: 440px;
    background: radial-gradient(ellipse 50% 50% at 50% 50%, var(--photo-red) 0%, rgba(154,16,20,0.45) 55%, rgba(5,5,7,0) 100%);
  }
  .brand {
    position: absolute;
    left: 0;
    top: 740px;
    width: 846px;
    text-align: center;
  }
  .brand-dot {
    display: block;
    width: 64px;
    height: 64px;
    margin: 0 auto;
    border-radius: 50%;
    background: var(--brand-red);
  }
  .brand-name {
    display: block;
    margin-top: 52px;
    font-size: 34px;
    font-weight: 400;
    line-height: 1;
    color: var(--brand-red);
  }
  .tagline {
    position: absolute;
    left: 0;
    top: 1012px;
    width: 846px;
    margin: 0;
    text-align: center;
    font-size: 26px;
    line-height: 1.2;
    letter-spacing: -0.3px;
    color: var(--paper-white);
  }
  .tagline-lead { font-weight: 600; }
  .tagline-emphasis { font-weight: 300; font-style: italic; }
  .website {
    position: absolute;
    left: 0;
    top: 1128px;
    width: 846px;
    text-align: center;
    font-size: 17px;
    font-weight: 300;
    letter-spacing: 3.5px;
    color: var(--muted-white);
  }
</style>
</head>
<body>
  <main class="ad">
    <div class="hero-photo" role="img" aria-label="Photograph of a glossy red apple with water droplets fading into a black background"></div>

    <div class="brand">
      <span class="brand-dot"></span>
      <span class="brand-name">Vantolix</span>
    </div>

    <p class="tagline">
      <span class="tagline-lead">Be in charge of</span>
      <span class="tagline-emphasis">your own health</span>
    </p>

    <div class="website">www.vantolix.co.uk.</div>
  </main>
</body>
</html>
```